Corwin Ashgrove

I am a songwriter and would like to include a bio, pictures, discography, CD covers and access to some of my music

Target Market(s)

Music Lovers, songwriters publishers

Coding

Coded - Design and coding required

Number of Pages Required

5+ page

Requirements
Must have
• Pictures of my CD covers, pictures of me and either my Music or links to my music
Nice to have
Should not have
• cartoons

```html
<!DOCTYPE html>
<html lang="en">
<head>
<meta charset="utf-8">
<title>Corwin Ashgrove — Songwriter</title>
<link href="https://fonts.googleapis.com/css2?family=Poppins:wght@400;500;600;700&display=swap" rel="stylesheet">
<style>
:root{
  --black:#000;
  --bio-bg:#1c1c1c;
  --music-bg:#2a2a2a;
  --review-bg:#1a1a1a;
  --white:#fff;
  --muted:#d6d6d6;
  --pill:#7a7a7a;
  --pill-dark:#111;
}
*{margin:0;padding:0;box-sizing:border-box}
html,body{width:1200px;height:4598px;overflow:hidden;background:var(--black)}
body{font-family:'Poppins',sans-serif;color:var(--white);position:relative}
.abs{position:absolute}
section,header,footer{position:absolute;left:0;width:1200px;overflow:hidden}

/* header + hero */
.hero{top:0;height:837px;background:var(--black)}
.hero-photo{position:absolute;inset:0;background:
  radial-gradient(ellipse 320px 420px at 740px 430px,#7d7d7d 0%,#4a4a4a 45%,transparent 75%),
  linear-gradient(176deg,#1a1a1a 0%,#1a1a1a 38%,#bdbdbd 44%,#6a6a6a 50%,#2a2a2a 62%,#111 100%)}
.hero-word{position:absolute;left:186px;top:392px;font-size:180px;font-weight:700;letter-spacing:4px;color:rgba(255,255,255,.18);line-height:1;white-space:nowrap}
.hero-title{position:absolute;left:191px;top:636px;font-size:38px;font-weight:400;line-height:50px}
.logo{position:absolute;font-weight:600;line-height:1.15;white-space:nowrap}
.logo-first::after{content:"";display:inline-block;width:44px;height:3px;background:var(--white);margin-left:14px;vertical-align:middle}
.site-logo{left:62px;top:30px;font-size:30px}
.nav{position:absolute;top:48px;left:0;font-size:15px}
.nav a{position:absolute;color:var(--white);text-decoration:none;white-space:nowrap}
.btn{position:absolute;display:flex;align-items:center;justify-content:center;border-radius:30px;font-weight:600;color:var(--white);text-decoration:none;white-space:nowrap}
.btn-song{left:857px;top:34px;width:136px;height:36px;background:var(--pill);font-size:10px}
.find-mini{position:absolute;left:1030px;top:26px;font-size:9px;white-space:nowrap}
.find-mini .names{display:block;margin-top:10px;font-size:8px;font-weight:600}

/* bio */
.bio{top:837px;height:620px;background:var(--bio-bg)}
.bio-name{left:75px;top:88px;font-size:26px}
.bio-heading{left:72px;top:124px;font-size:43px;font-weight:700}
.bio-text{left:441px;top:82px;width:700px;font-size:15.2px;line-height:31.2px}
.btn-read{left:441px;top:436px;width:157px;height:54px;background:var(--pill);font-size:14px}
.music-edge{position:absolute;left:0;bottom:0}

/* music */
.music{top:1455px;height:1038px;background:var(--music-bg)}
.section-heading{position:absolute;left:0;width:1200px;text-align:center;font-weight:700;font-size:43px}
.music .section-heading{top:30px}
.cover{position:absolute;width:292px;height:292px}
.cover-1{left:89px;top:204px;background:linear-gradient(160deg,#5a5d7a,#262233 55%,#8a3a1c)}
.cover-2{left:450px;top:204px;background:linear-gradient(135deg,#f5eebb,#d6e6ef 50%,#f2c9d6)}
.cover-3{left:807px;top:204px;background:linear-gradient(180deg,#4d6b83,#e7eef0 50%,#2f4d62 80%,#b88a2e)}
.cover-4{left:95px;top:560px;background:linear-gradient(150deg,#e8532a,#f3b23b 45%,#8c8f88)}
.cover-5{left:450px;top:560px;background:linear-gradient(135deg,#ec2f8a,#7a4fc9 50%,#34c2d9)}
.cover-6{left:807px;top:560px;background:linear-gradient(135deg,#e2262a,#1d3fae 40%,#f4d21b 70%,#111)}
.btn-all{left:486px;top:913px;width:200px;height:57px;background:var(--pill-dark);font-size:14px}

/* find music */
.find{top:2493px;height:268px;background:var(--black)}
.find .section-heading{top:38px}
.platforms{position:absolute;top:132px;left:0;width:1200px;display:flex;justify-content:center;gap:60px}
.platform{display:flex;align-items:center;gap:12px;font-size:26px;font-weight:600}
.platform::before{content:"";width:40px;height:40px;border-radius:50%;background:var(--white)}

/* reviews */
.reviews{top:2761px;height:557px;background:radial-gradient(ellipse at 60% 60%,#2b2b2b,var(--review-bg) 70%)}
.reviews .section-heading{top:70px}
.review-text{position:absolute;left:196px;top:164px;width:758px;text-align:center;font-size:15.5px;line-height:25px;color:var(--muted)}
.review-author{position:absolute;left:0;top:362px;width:1200px;text-align:center;font-size:18px;font-weight:600}
.arrow{position:absolute;top:196px}
.dots{position:absolute;top:437px;left:426px;display:flex;gap:20px}
.dot{width:17px;height:17px;border:2px solid var(--white);border-radius:50%;position:relative}
.dot::after{content:"";position:absolute;left:4px;top:4px;width:5px;height:5px;border-radius:50%;background:var(--white)}
.dot.active{background:var(--white)}

/* news */
.news{top:3318px;height:650px;background:var(--black)}
.news .section-heading{top:56px}
.post{position:absolute;top:182px;width:322px}
.post-1{left:104px}.post-2{left:454px}.post-3{left:804px}
.post-image{width:322px;height:233px;background:linear-gradient(160deg,#c9c9c9,#4a4a4a 60%,#1d1d1d)}
.post-2 .post-image{background:linear-gradient(180deg,#3d7bd0 0%,#8fb4e1 30%,#7f8a3a 35%,#a78a44 70%,#6b5a2a)}
.post-title{margin-top:24px;font-size:18px;font-weight:600;line-height:31px;text-transform:uppercase}
.post-text{margin-top:10px;font-size:14.5px;line-height:25px;color:var(--muted)}

/* cta */
.cta{top:3968px;height:416px;background:radial-gradient(ellipse at 50% 40%,#2d2d2d,#141414 75%)}
.cta .section-heading{top:188px}
.btn-line{left:489px;top:277px;width:186px;height:52px;background:var(--pill-dark);font-size:18px;font-weight:400}

/* footer */
.footer{top:4384px;height:214px;background:var(--black)}
.footer-logo{left:164px;top:50px;font-size:30px}
.contact{position:absolute;left:391px;top:50px;width:400px;text-align:center;font-size:18px;line-height:32px}
.follow{position:absolute;left:842px;top:40px;width:230px;text-align:center;font-size:18px}
.follow .names{display:block;margin-top:8px;font-size:11px;font-weight:600;white-space:nowrap}
.copyright{position:absolute;left:0;top:178px;width:1200px;text-align:center;font-size:9px;color:var(--muted)}
</style>
</head>
<body>

<header class="hero">
  <div class="hero-photo" role="img" aria-label="Black and white photo of the songwriter standing at night in front of a glowing rock crater"></div>
  <div class="hero-word">CORWIN</div>
  <h1 class="hero-title">Corwin Ashgrove<br>is a songwriter<br>based in Houston, Texas</h1>
  <div class="logo site-logo"><span class="logo-first">Corwin</span><br>Ashgrove</div>
  <nav class="nav">
    <a style="left:368px" href="#">HOME</a>
    <a style="left:463px" href="#">BIO</a>
    <a style="left:539px" href="#">MUSIC</a>
    <a style="left:634px" href="#">BLOGS</a>
    <a style="left:730px" href="#">CONTACT</a>
  </nav>
  <a class="btn btn-song" href="#">WRITE ME A SONG</a>
  <div class="find-mini">Find my music on<span class="names">PhotoLoop · StreamNest · ClipTower</span></div>
</header>

<section class="bio">
  <div class="abs bio-name">Corwin Ashgrove</div>
  <h2 class="abs bio-heading">BIOGRAPHY</h2>
  <p class="abs bio-text">Corwin Ashgrove was born and raised in Houston, Texas. He began playing music at the age of eight when his sister returned home from summer camp and asked her parents to buy her a baritone ukulele. She taught her younger brother some chords on the ukulele and he was hooked. The following spring, they went to one of the border towns in Mexico and bought a Mexican guitar for $12. They restrung it with nylon strings and Ashgrove began to learn how to play the guitar. He took guitar lessons at a local music store and learned how to play the hits of the day by groups like the Larkspur Five, the Copper Wolves, and the Marigolds. He got his first electric guitar when he was about 10 years old. He began jamming with other musicians when he was 13 or 14. They were much more experienced than he and introduced him to the blues.</p>
  <a class="btn btn-read" href="#">READ MORE</a>
  <svg class="music-edge" width="1200" height="50" viewBox="0 0 1200 50"><polygon points="0,45 410,2 1200,32 1200,50 0,50" fill="#2a2a2a"/></svg>
</section>

<section class="music">
  <h2 class="section-heading">MUSIC</h2>
  <div class="cover cover-1" role="img" aria-label="Album cover: silhouette under a lightning storm over a burning town"></div>
  <div class="cover cover-2" role="img" aria-label="Album cover: pastel collage with a child's photo"></div>
  <div class="cover cover-3" role="img" aria-label="Album cover: waves crashing against rocks"></div>
  <div class="cover cover-4" role="img" aria-label="Album cover: burning cash on a diner table with a coffee cup"></div>
  <div class="cover cover-5" role="img" aria-label="Album cover: musician with a mandolin on a colourful swirl"></div>
  <div class="cover cover-6" role="img" aria-label="Album cover: colourful abstract hand-painted pattern"></div>
  <a class="btn btn-all" href="#">VIEW ALL MUSIC</a>
</section>

<section class="find">
  <h2 class="section-heading">FIND &nbsp;MY MUSIC ON</h2>
  <div class="platforms">
    <span class="platform">PhotoLoop</span>
    <span class="platform">StreamNest</span>
    <span class="platform">ClipTower</span>
  </div>
</section>

<section class="reviews">
  <h2 class="section-heading">REVIEWS</h2>
  <svg class="arrow" style="left:52px" width="36" height="70" viewBox="0 0 36 70"><polyline points="34,2 2,35 34,68" fill="none" stroke="#fff" stroke-width="2"/></svg>
  <svg class="arrow" style="left:1110px" width="36" height="70" viewBox="0 0 36 70"><polyline points="2,2 34,35 2,68" fill="none" stroke="#fff" stroke-width="2"/></svg>
  <p class="review-text">If you are looking for superior wring and song composition then Corwin is your guy. Not only is he truly a professional, He has a unique style and extremely engaging storytelling. I am wowed every time!!! 10 stars! ★★★★★★★★★★ Once again Corwin delivers an AMAZING SONG! I still can't believe how thoughtful and precise Corwin's writing skills are. Phenomenal :) Corwin is a rare breed. His lyrical content and melody selections are superb. He addresses current events via his music with a point of view that really engages you. His musical talents are inspiring. He knows what he is doing point blank period! :)</p>
  <div class="review-author">Golden Reel Nominated Songwriter Vocals</div>
  <div class="dots">
    <span class="dot"></span><span class="dot active"></span><span class="dot"></span><span class="dot"></span><span class="dot"></span>
    <span class="dot"></span><span class="dot"></span><span class="dot"></span><span class="dot"></span><span class="dot"></span>
  </div>
</section>

<section class="news">
  <h2 class="section-heading">WHAT'S NEW</h2>
  <article class="post post-1">
    <div class="post-image" role="img" aria-label="Black and white photo of a guitarist seated outdoors"></div>
    <h3 class="post-title">New song released</h3>
    <p class="post-text">Hey Everyone! I'm so excited to start releasing new music into the world and I can't wait for ya'll to hear this one.</p>
  </article>
  <article class="post post-2">
    <div class="post-image" role="img" aria-label="Red chair with a guitar in a golden field under blue sky"></div>
    <h3 class="post-title">First show is officially sold out</h3>
    <p class="post-text">Don't worry, we added a second show on January 15th 2021</p>
  </article>
  <article class="post post-3">
    <div class="post-image" role="img" aria-label="Black and white photo of a guitarist seated outdoors"></div>
    <h3 class="post-title">Pre-save “Open Palms”<br>now on StreamNest</h3>
    <p class="post-text">I'm really excited to be working with the amazing folks at StreamNest,</p>
  </article>
</section>

<section class="cta">
  <h2 class="section-heading">READY TO START A PROJECT?</h2>
  <a class="btn btn-line" href="#">Drop me a line</a>
</section>

<footer class="footer">
  <div class="logo footer-logo"><span class="logo-first">Corwin</span><br>Ashgrove</div>
  <div class="contact">+44 555 00 00 27<br>corwin.ashgrove@example.com</div>
  <div class="follow">Follow me on<span class="names">PageCircle · QuickPost · ClipTower</span></div>
  <div class="copyright">© 2020 Corwin Ashgrove. All rights reserved.</div>
</footer>

</body>
</html>
```